Comparison Website Design for Glue Website

Note: We don't have a logo, it's not needed. Just put placeholder.

We would like a website comparing A to B, simple elegant design, simplistic styling. Website is for helping people find the best glue to glue 2 things together. For example, Metal to wood, Metal to rubber, glass to fabric and so on. Select 2 options and be shown the best glue/adhesive for the job.

Purpose of the website:
Allowing someone to pick 2 materials they want to glue together, and showing them the best product for it. We want someone to select 2 materials like "Metal and Rubber". It'll then show the best glues/adhesives from best #1 to #5-10 other ones. The design is simple and doesn't need much detail.

Design rules:
Please design using bootstrap 4 with a modified 1440px width.

We're looking for 4 main pages:
Home Page, Compare Page, Category Page, Product Page.

Target Market(s)

Everyone

Industry/Entity Type

Adhesive

Number of Pages Required

3 page

Font styles to use
Sans Serif

Colors
876aae
b7a5cd
6b449b
e4daeb
fefeff

Requirements
Must have
• We like the following features of these designs:
https://pixlorum.net/works/7310284-Cavrano-Dashboard - Main menu with the drop down, this will change depending on the active page. If they are on a metal page they could be shown "glue metal to ___" options. We also like the simple table view in this design under "users" heading.

https://pixlorum.net/works/7228451-Quotation-Page - The entire colour palette is great! The simplicity of the design is great.

https://pixlorum.net/works/9107642-Comparison-UI - The boxes at the top look great, if there was 2 of these with a compare icon between them and above that saying "glue metal to rubber" and it shows an icon/image or metal and glue... The table of products is also good, it has dot points and details which we like.

https://pixlorum.net/works/5093718-Send-Funds/attachments/5093718-Send-Funds?mode=media - The right it shows which 2 products are selected (metal and rubber) for example, on the left it would say "best glue for metal and rubber". This is too detailed though, so it would need to be simplified nicely.

https://linquora.net/ - They do a good job of "comparing" 2 things and displaying integrations well. You can get lots of ideas from them linking A to B similar to what we want to show.

https://www.flowtoolreviewdesk.net/brivelo-vs-tandrix/ - This shows a good example of the hero section how it should look.

Features of each page to help you design:
Home Page-
Menu (shown in examples above)
Hero section (colour section) with a centre heading saying "what do you want to glue together" with 2 boxes below to select materials from.
List of most popular searches (metal to rubber, glass to wood, fabric to leather... repeat these to fill space).
List of popular products with basic details about each one (grid format, not list).
FAQs - You choose design for this
Content section (simple design, headings, paragraphs, dotpoints, images...)
Blog section - Simple 3 column grid with an image on top, heading, paragraph, button.

Compare Page-
Showing 2 materials in the colour hero section under or to the right of the heading and paragraph.
Best product (highlighted)
9 other products (list table)
3 column section saying glue (product a to ___) with other product that isn't product b + reverse of this.
Content section

Category page-
heading and breadcrumbs in hero section
Standard product list 1 column on the left with filters, 3 products shown on the right in grid format with basic details on each one.

Product page-
Image left, details on the right.
Keep the image smaller not 50% as we want it to not take up too much space vertically.
Under this put a table where this product ranks for gluing things together. for example #3 for gluing metal to rubber, #1 for glass to wood.
Content section.

Please note, keep this design flat, simple and pretty. We don't need it over-designed or detailed, we simply want a simple functionality website that clearly shows what we're looking for.

```html
<!DOCTYPE html>
<html lang="en">
<head>
<meta charset="utf-8">
<title>Bondwise</title>
<link href="https://fonts.googleapis.com/css2?family=Lato:wght@400;700;900&display=swap" rel="stylesheet">
<style>
:root{
  --purple:#6b449b;
  --purple-mid:#876aae;
  --purple-soft:#b7a5cd;
  --lilac:#e4daeb;
  --lilac-bg:#f3edf9;
  --white:#fefeff;
  --ink:#222226;
  --text:#3a3a42;
  --muted:#8b8b94;
  --line:#e6e2ec;
  --green:#3fb24a;
  --red:#e23b4a;
  --star:#e9b92c;
  --footer:#222;
}
*{box-sizing:border-box;margin:0;padding:0}
html,body{width:1200px;height:4092px;overflow:hidden}
body{font-family:"Lato",sans-serif;color:var(--text);background:var(--white);position:relative}
.section-title{font-weight:900;font-size:52px;color:var(--ink);text-align:center;letter-spacing:-.5px}
.btn{display:inline-flex;align-items:center;justify-content:center;background:var(--purple);color:#fff;font-weight:900;text-transform:uppercase;border-radius:30px;text-decoration:none}

/* header */
.site-header{position:absolute;top:0;left:0;width:1200px;height:83px;background:#fff}
.brand{position:absolute;left:126px;top:18px;font-size:32px;font-weight:900;color:var(--purple)}
.main-nav{position:absolute;left:632px;top:30px;font-size:15px;color:var(--ink)}
.main-nav a{color:inherit;text-decoration:none;position:absolute;white-space:nowrap}
.main-nav .active{border-bottom:2px solid var(--purple);padding-bottom:6px}
.login{position:absolute;left:977px;top:26px;width:96px;height:32px;font-size:14px}

/* hero */
.hero{position:absolute;top:83px;left:0;width:1200px;height:575px;
  background:radial-gradient(ellipse at 80% 20%,#7b1ea8 0%,transparent 55%),radial-gradient(ellipse at 10% 90%,#9a1c9a 0%,transparent 50%),linear-gradient(135deg,#3d1670 0%,#5a1a8c 50%,#3a0f66 100%)}
.hero h1{position:absolute;top:132px;width:100%;text-align:center;color:#fff;font-size:54px;font-weight:900;letter-spacing:-.5px}
.material-box{position:absolute;top:267px;width:246px;height:158px;background:rgba(183,165,205,.45);border-bottom:7px solid rgba(183,165,205,.75);color:#fff;text-align:center}
.material-box svg{margin-top:26px}
.material-box span{display:block;margin-top:10px;font-weight:900;font-size:20px}
.vs{position:absolute;left:566px;top:313px;width:66px;height:66px;border:1.5px dashed rgba(255,255,255,.6);border-radius:50%;color:#fff;font-size:24px;display:flex;align-items:center;justify-content:center}
.slider-dots{position:absolute;top:521px;left:577px;display:flex;gap:5px}
.slider-dots i{width:8px;height:8px;border-radius:50%;background:#fff}

/* searches */
.searches{position:absolute;top:658px;left:0;width:1200px;height:750px}
.searches .section-title{position:absolute;top:84px;width:100%}
.search-card{position:absolute;top:205px;width:295px;height:453px;border:1px solid var(--line);background:#fff}
.search-card header{margin:13px 13px 0;height:86px;background:#efe8f7;text-align:center;padding-top:24px}
.search-card h3{font-size:25px;font-weight:700;color:var(--purple-mid)}
.stars{color:var(--star);font-size:12px;letter-spacing:3px;margin-top:4px}
.search-card ul{list-style:none;margin:34px 0 0 33px}
.search-card li{height:31px;display:flex;align-items:center;font-size:14px;color:var(--text)}
.search-card li svg{margin-right:18px;flex:none}
.search-card .btn{position:absolute;left:60px;top:375px;width:175px;height:44px;font-size:13px}

/* products */
.products{position:absolute;top:1408px;left:0;width:1200px;height:612px;background:var(--lilac-bg)}
.products .section-title{position:absolute;top:74px;width:100%}
.product-card{position:absolute;top:181px;width:227px;height:350px;background:#fff;border:1px solid var(--line);text-align:center}
.product-img{height:150px;margin:2px 2px 0}
.product-card h3{margin-top:22px;font-size:18px;font-weight:700;color:var(--purple-mid)}
.product-card .stars{font-size:10px;margin-top:8px}
.product-card p{margin-top:8px;font-size:13px;line-height:20px}
.product-card .btn{margin-top:14px;width:135px;height:35px;font-size:11px}
.arrow{position:absolute;top:334px;width:46px;height:46px;border:1.5px solid #666;border-radius:50%;background:#fff;display:flex;align-items:center;justify-content:center}

/* faq */
.faq{position:absolute;top:2020px;left:0;width:1200px;height:586px}
.faq .section-title{position:absolute;top:80px;width:100%}
.faq-item{position:absolute;left:281px;width:636px;height:51px;border:1px solid var(--line);border-radius:26px;background:#fff;display:flex;align-items:center;padding-left:36px;font-size:15px;font-weight:700;color:var(--ink)}
.faq-item b{position:absolute;right:6px;top:8px;width:35px;height:35px;border-radius:50%;background:var(--purple);color:#fff;display:flex;align-items:center;justify-content:center;font-size:22px}
.faq-answer{position:absolute;left:310px;top:250px;width:580px;font-size:12.5px;line-height:24px;color:var(--muted)}

/* about */
.about{position:absolute;top:2606px;left:0;width:1200px;height:625px;background:#f1f1f4}
.about .wave{position:absolute;top:0;left:0}
.about h2{position:absolute;left:126px;top:182px;font-size:54px;font-weight:900;color:var(--ink)}
.about p{position:absolute;left:126px;top:264px;width:500px;font-size:13px;line-height:26px;color:var(--text)}
.about .btn{position:absolute;left:126px;top:504px;width:134px;height:35px;font-size:12px}
.about-art{position:absolute;left:656px;top:119px;width:499px;height:393px;border-radius:8px;background:linear-gradient(160deg,#e9e4f0,#dcd6e6)}

/* blog */
.blog{position:absolute;top:3231px;left:0;width:1200px;height:783px}
.blog .section-title{position:absolute;top:80px;width:100%}
.blog-card{position:absolute;top:190px;width:310px;height:512px;border:1px solid var(--line);background:#fff}
.blog-img{height:233px;margin:3px 3px 0}
.blog-card time{display:block;margin:40px 0 0 23px;font-size:14px;color:var(--purple-mid)}
.blog-card h3{margin:16px 8px 0 23px;font-size:19px;font-weight:700;line-height:27px;color:var(--ink)}
.blog-card p{margin:18px 0 0 23px;width:260px;font-size:13px;line-height:22px;color:var(--muted)}
.blog-card .btn{margin:24px 0 0 23px;width:135px;height:35px;font-size:12px}

/* footer */
.site-footer{position:absolute;top:4014px;left:0;width:1200px;height:78px;background:var(--footer);color:#fff}
.site-footer .legal{position:absolute;left:126px;top:31px;font-size:12px}
.site-footer .legal span{margin:0 6px}
.social{position:absolute;left:821px;top:18px;display:flex;gap:10px}
.social i{width:42px;height:42px;border:1.5px solid #fff;border-radius:50%}
</style>
</head>
<body>

<header class="site-header">
  <div class="brand">Bondwise</div>
  <nav class="main-nav">
    <a class="active" style="left:0">Home</a>
    <a style="left:72px">Compare</a>
    <a style="left:166px">Category</a>
    <a style="left:261px">Product</a>
  </nav>
  <a class="btn login">Login</a>
</header>

<section class="hero">
  <h1>What do you want to glue together</h1>
  <div class="material-box" style="left:302px">
    <svg width="70" height="62" viewBox="0 0 70 62" fill="none" stroke="#fff" stroke-width="2.5"><circle cx="17" cy="16" r="12"/><circle cx="17" cy="16" r="5"/><circle cx="53" cy="16" r="12"/><circle cx="53" cy="16" r="5"/><circle cx="35" cy="40" r="12"/><circle cx="35" cy="40" r="5"/><circle cx="12" cy="52" r="3"/><circle cx="58" cy="52" r="3"/></svg>
    <span>METAL</span>
  </div>
  <div class="vs">VS</div>
  <div class="material-box" style="left:651px">
    <svg width="80" height="62" viewBox="0 0 80 62" fill="none" stroke="#fff" stroke-width="3"><ellipse cx="40" cy="26" rx="36" ry="22"/><ellipse cx="40" cy="26" rx="22" ry="11"/><path d="M4 26v10c0 12 16 22 36 22s36-10 36-22V26"/></svg>
    <span>RUBBER</span>
  </div>
  <div class="slider-dots"><i></i><i></i><i></i><i></i></div>
</section>

<section class="searches">
  <h2 class="section-title">Most Popular Searches</h2>
  <svg width="0" height="0" style="position:absolute"><defs>
    <symbol id="ok" viewBox="0 0 14 14"><circle cx="7" cy="7" r="7" fill="#3fb24a"/><path d="M4 7.2l2 2 4-4" stroke="#fff" stroke-width="1.8" fill="none"/></symbol>
    <symbol id="no" viewBox="0 0 14 14"><circle cx="7" cy="7" r="7" fill="#e23b4a"/><path d="M4.5 4.5l5 5M9.5 4.5l-5 5" stroke="#fff" stroke-width="1.8"/></symbol>
  </defs></svg>
  <article class="search-card" style="left:126px">
    <header><h3>Metal to rubber</h3><div class="stars">★★★★★</div></header>
    <ul>
      <li><svg width="14" height="14"><use href="#ok"/></svg>Sed ut perspiciatis unde omnis</li>
      <li><svg width="14" height="14"><use href="#ok"/></svg>Iste natus error sit voluptatem</li>
      <li><svg width="14" height="14"><use href="#ok"/></svg>Accusantium doloremque</li>
      <li><svg width="14" height="14"><use href="#ok"/></svg>Laudantiumotam rem aperia</li>
      <li><svg width="14" height="14"><use href="#ok"/></svg>Eaque ipsa quae ab illo inven</li>
      <li><svg width="14" height="14"><use href="#no"/></svg>Toreeritatis et quarchitecto</li>
      <li><svg width="14" height="14"><use href="#no"/></svg>Beatae vitae dicta sxplicabo</li>
    </ul>
    <a class="btn">Learn More</a>
  </article>
  <article class="search-card" style="left:453px">
    <header><h3>Glass to Wood</h3><div class="stars">★★★★★</div></header>
    <ul>
      <li><svg width="14" height="14"><use href="#ok"/></svg>Sed ut perspiciatis unde omnis</li>
      <li><svg width="14" height="14"><use href="#ok"/></svg>Iste natus error sit voluptatem</li>
      <li><svg width="14" height="14"><use href="#ok"/></svg>Accusantium doloremque</li>
      <li><svg width="14" height="14"><use href="#ok"/></svg>Laudantiumotam rem aperia</li>
      <li><svg width="14" height="14"><use href="#ok"/></svg>Eaque ipsa quae ab illo inven</li>
      <li><svg width="14" height="14"><use href="#no"/></svg>Toreeritatis et quarchitecto</li>
      <li><svg width="14" height="14"><use href="#no"/></svg>Beatae vitae dicta sxplicabo</li>
    </ul>
    <a class="btn">Learn More</a>
  </article>
  <article class="search-card" style="left:779px">
    <header><h3>Fabric to Leather</h3><div class="stars">★★★★★</div></header>
    <ul>
      <li><svg width="14" height="14"><use href="#ok"/></svg>Sed ut perspiciatis unde omnis</li>
      <li><svg width="14" height="14"><use href="#ok"/></svg>Iste natus error sit voluptatem</li>
      <li><svg width="14" height="14"><use href="#ok"/></svg>Accusantium doloremque</li>
      <li><svg width="14" height="14"><use href="#ok"/></svg>Laudantiumotam rem aperia</li>
      <li><svg width="14" height="14"><use href="#ok"/></svg>Eaque ipsa quae ab illo inven</li>
      <li><svg width="14" height="14"><use href="#no"/></svg>Toreeritatis et quarchitecto</li>
      <li><svg width="14" height="14"><use href="#no"/></svg>Beatae vitae dicta sxplicabo</li>
    </ul>
    <a class="btn">Learn More</a>
  </article>
</section>

<section class="products">
  <h2 class="section-title">Popular Products</h2>
  <div class="arrow" style="left:53px"><svg width="12" height="20"><path d="M10 2L2 10l8 8" stroke="#444" stroke-width="2" fill="none"/></svg></div>
  <article class="product-card" style="left:126px">
    <div class="product-img" role="img" aria-label="Stack of steel pipes" style="background:linear-gradient(180deg,#f4f4f6,#b9bcc2 60%,#f4f4f6)"></div>
    <h3>Product Name</h3><div class="stars">★★★★★</div>
    <p>Lorem ipsum dolor sit amet<br>consectetur adipiscing</p>
    <a class="btn">View Details</a>
  </article>
  <article class="product-card" style="left:366px">
    <div class="product-img" role="img" aria-label="Black rubber car floor mats" style="background:radial-gradient(ellipse at center,#3a3a3e 0%,#5c5c62 45%,#fff 72%)"></div>
    <h3>Product Name</h3><div class="stars">★★★★★</div>
    <p>Lorem ipsum dolor sit amet<br>consectetur adipiscing</p>
    <a class="btn">View Details</a>
  </article>
  <article class="product-card" style="left:607px">
    <div class="product-img" role="img" aria-label="Clear glass sphere" style="background:radial-gradient(circle at center,#fafafa 0%,#dcdcdf 45%,#fff 50%)"></div>
    <h3>Product Name</h3><div class="stars">★★★★★</div>
    <p>Lorem ipsum dolor sit amet<br>consectetur adipiscing</p>
    <a class="btn">View Details</a>
  </article>
  <article class="product-card" style="left:847px">
    <div class="product-img" role="img" aria-label="Cross section of a tree log" style="background:radial-gradient(circle at center,#e4b774 0%,#c98c4a 38%,#6b4326 46%,#fff 48%)"></div>
    <h3>Product Name</h3><div class="stars">★★★★★</div>
    <p>Lorem ipsum dolor sit amet<br>consectetur adipiscing</p>
    <a class="btn">View Details</a>
  </article>
  <div class="arrow" style="left:1099px"><svg width="12" height="20"><path d="M2 2l8 8-8 8" stroke="#444" stroke-width="2" fill="none"/></svg></div>
</section>

<section class="faq">
  <h2 class="section-title">FAQs</h2>
  <div class="faq-item" style="top:181px">Lorem ipsum dolor sit ametconsectetur adipiscing elit?<b>–</b></div>
  <p class="faq-answer">Lorem ipsum dolor sit amet, consectetur adipiscing elit, sed do eiusmod tempor incididunt ut labore et dolore magna aliqua. Ut enim ad minim veniam, quis nostrud exercitation ullamco laboris nisi ut aliquip ex lor in reprehenderit in voluptate velit esse</p>
  <div class="faq-item" style="top:332px">Sed ut perspiciatis unde omnis iste natus error sit?<b>+</b></div>
  <div class="faq-item" style="top:392px">Iunde omnis iste natus error sit voluptatem accusantium ?<b>+</b></div>
  <div class="faq-item" style="top:453px">Lorem ipsum dolor sit ametconsectetur adipiscing elit?<b>+</b></div>
</section>

<section class="about">
  <svg class="wave" width="1200" height="110" viewBox="0 0 1200 110"><path d="M0 0H1200V40C1100 10 1000 50 900 30C760 0 640 10 520 30C380 55 240 20 120 30C60 35 20 45 0 50Z" fill="#fff"/><path d="M20 60C140 20 280 30 380 55C300 80 160 95 20 60Z" fill="#dfe2ea"/><path d="M1080 60C1130 40 1170 38 1200 40V80C1160 80 1110 75 1080 60Z" fill="#dfe2ea"/></svg>
  <h2>About Us</h2>
  <p>Lorem ipsum dolor sit amet, consectetur adipiscing elit, sed do eiusmod tempor incididunt ut labore et dolore magna aliqua. is ipsum suspendisse ultrices gravida. Risus commodo viverra maecenas accumsan lacus vel facilisisrem ipsum dolor sit amet, consectetur adipiscing elit, sed do eiusmod tempor incididunt ut labore et dolore magna aliquais ipsum suspendisse ultrices gravidasus commodo viverra maecenas accumsan lacus vel facilim ipsum dolor sit amet, consectetur adipiscing elit, sed do eiusmod tempor incididunt ut labore et dolore magna aliquais ipsum suspendisse ultrices gramodo viverra maecenas accumsan laciuel facilisis.</p>
  <a class="btn">Read More</a>
  <div class="about-art" role="img" aria-label="Illustration of a person next to a document linked to three smaller documents"></div>
</section>

<section class="blog">
  <h2 class="section-title">Blog Posts</h2>
  <article class="blog-card" style="left:121px">
    <div class="blog-img" role="img" aria-label="Riveted brushed metal plates" style="background:linear-gradient(135deg,#d8d9dc,#9c9ea3 50%,#c9cacd)"></div>
    <time>December 22,2020</time>
    <h3>Sed ut perspiciatis undeomnis iste natus voluptatem</h3>
    <p>Ut enim ad minima venias nostreierci tationem ullam corporis suscipitboriosan isi ut aliquid ex ea commodihenderitq ui in ea voluptate velit .</p>
    <a class="btn">Read More</a>
  </article>
  <article class="blog-card" style="left:445px">
    <div class="blog-img" role="img" aria-label="Dark wooden planks" style="background:linear-gradient(90deg,#4a2c18,#8a5a33 30%,#5e3a20 55%,#9a6a3d 80%,#4a2c18)"></div>
    <time>December 22,2020</time>
    <h3>Sed ut perspiciatis undeomnis iste natus voluptatem</h3>
    <p>Ut enim ad minima venias nostreierci tationem ullam corporis suscipitboriosan isi ut aliquid ex ea commodihenderitq ui in ea voluptate velit .</p>
    <a class="btn">Read More</a>
  </article>
  <article class="blog-card" style="left:769px">
    <div class="blog-img" role="img" aria-label="Black quilted leather" style="background:radial-gradient(ellipse at center,#2e2e30,#0d0d0e)"></div>
    <time>December 22,2020</time>
    <h3>Sed ut perspiciatis undeomnis iste natus voluptatem</h3>
    <p>Ut enim ad minima venias nostreierci tationem ullam corporis suscipitboriosan isi ut aliquid ex ea commodihenderitq ui in ea voluptate velit .</p>
    <a class="btn">Read More</a>
  </article>
</section>

<footer class="site-footer">
  <div class="legal">Copyrights © 2020 Bondwise.All rights reserved<span>|</span>Privacy policy<span>|</span>Site Map<span>|</span>Disclaimer<span>|</span>Terms of use</div>
  <div class="social" aria-label="Social links"><i></i><i></i><i></i><i></i><i></i></div>
</footer>

</body>
</html>
```